Harbor Deed needs a new brochure design

The brochure will be used as a marketing tool for Realtors, Lenders and Family Law Attorney's. I have attached the "OLD" brochure to give you an idea of our business and what we do. We want a fresh more modern design. I also attached the Logo. Please let me know if you need any further information

Target Market(s)

Realtors, mortgage professionals (home lenders), Family Law Attorneys

```html
<!DOCTYPE html>
<html lang="en">
<head>
<meta charset="utf-8">
<title>Harbor Deed Brochure</title>
<link rel="stylesheet" href="https://fonts.googleapis.com/css2?family=Oswald:wght@300;500;700&family=Roboto:ital,wght@0,400;0,500;0,700;1,400;1,700&family=Montserrat:wght@600&display=swap">
<style>
:root{
  --blue:#0c2f8f;
  --blue-dark:#0a2676;
  --slate:#56646b;
  --ink:#333a40;
  --paper:#ffffff;
  --stage:#e4e4e4;
}
*{box-sizing:border-box;margin:0;padding:0}
html,body{width:779px;height:1200px;overflow:hidden;background:var(--stage)}
body{position:relative;font-family:'Roboto',Arial,sans-serif;color:var(--ink)}
.spread{position:absolute;left:30px;width:719px;height:512px;background:var(--paper);overflow:hidden;box-shadow:0 4px 12px rgba(0,0,0,.18)}
.spread--cover{top:55px}
.spread--inside{top:615px}
.spread .fold{position:absolute;left:359px;top:0;width:14px;height:100%;background:linear-gradient(90deg,rgba(0,0,0,.08),rgba(0,0,0,0));pointer-events:none}
.art{position:absolute;left:0;top:0}
.abs{position:absolute}
.heading{font-family:'Oswald',sans-serif;font-weight:300;color:var(--blue);letter-spacing:.2px;text-transform:uppercase;line-height:1}
.heading b{font-weight:700}
.body-copy{font-size:6.4px;line-height:1.3;text-align:justify;color:var(--ink)}
.body-copy p+p{margin-top:5px}
.lead{font-style:italic;font-weight:700;font-size:7px;line-height:1.3;color:var(--ink)}
.brand{font-family:'Montserrat',sans-serif;font-weight:600;color:#2a2f35;letter-spacing:2px;display:flex;align-items:center;gap:6px;white-space:nowrap}
.brand .mark{display:inline-block;background:var(--blue)}
.contact-title{font-weight:700;font-size:10px;color:#222}
.address{font-size:7px;line-height:1.35}
.contact-list{list-style:none;font-size:7.4px;line-height:1.75;color:#222}
.contact-list li{display:flex;align-items:center;gap:5px}
.contact-list svg{width:8px;height:8px;fill:var(--blue)}
.tagline{color:#fff;text-align:center;width:359px}
.tagline .intro{font-family:'Oswald',sans-serif;font-weight:300;font-size:15.5px}
.tagline .big{font-family:'Montserrat',sans-serif;font-weight:600;font-size:14.5px;letter-spacing:.8px;line-height:1.25;margin-top:6px}
.pill{display:inline-block;background:var(--blue);color:#fff;font-size:9.5px;padding:3px 16px;border-radius:10px;margin-top:9px}
.url{font-size:8px;letter-spacing:1.6px;color:#dfe3e5;margin-top:9px}
.apart-title{font-family:'Oswald',sans-serif;font-weight:300;font-size:19px;color:#fff;text-transform:uppercase;line-height:1}
.apart-title b{font-weight:500}
.apart-box{background:var(--blue);color:#fff;padding:9px 9px;font-size:6.6px;line-height:1.3}
.apart-box p{text-align:justify}
.apart-box p+p{margin-top:6px}
.apart-box h4{font-style:italic;font-weight:700;font-size:8.4px;margin:9px 0 6px}
.innovations{list-style:none}
.innovations li{display:flex;gap:7px;margin-bottom:7px;font-size:6.4px;line-height:1.3}
.innovations svg{flex:none;width:8px;height:8px;fill:#fff;margin-top:1px}
.apart-box .note{font-style:italic;font-weight:700;font-size:8px;line-height:1.25;margin-top:2px;text-align:left}
.footer-band{position:absolute;left:0;top:476px;width:360px;height:36px;background:var(--slate);color:#fff;font-family:'Montserrat',sans-serif;font-weight:600;font-size:11px;letter-spacing:2px;padding:12px 0 0 32px}
.seal{color:#fff;text-align:center;font-family:'Oswald',sans-serif;line-height:1.1}
.seal span{display:block;font-weight:300;font-size:22px}
.seal b{display:block;font-weight:700;font-size:22px}
</style>
</head>
<body>

<!-- Cover spread -->
<section class="spread spread--cover">
  <svg class="art" width="719" height="512" viewBox="0 0 719 512">
    <defs>
      <linearGradient id="gPorch" x1="0" y1="0" x2="1" y2="1"><stop offset="0" stop-color="#9aa39a"/><stop offset="1" stop-color="#6e7a63"/></linearGradient>
      <linearGradient id="gCouple" x1="0" y1="0" x2="1" y2="1"><stop offset="0" stop-color="#e9e1d8"/><stop offset=".5" stop-color="#c9b5a4"/><stop offset="1" stop-color="#9a9fa5"/></linearGradient>
      <radialGradient id="gHouse"><stop offset="0" stop-color="#d9a98c"/><stop offset="1" stop-color="#f6ece6"/></radialGradient>
    </defs>
    <rect x="360" y="331" width="359" height="181" fill="var(--slate)"/>
    <rect x="0" y="131" width="120" height="21" fill="var(--blue)"/>
    <path d="M120 151H268L308 230L268 312H0" fill="none" stroke="var(--blue)" stroke-width="1"/>
    <g role="img" aria-label="Photo: couple shaking hands with a real estate agent by a for-sale sign">
      <polygon points="0,153 265,153 304,230 265,310 0,310" fill="url(#gPorch)"/>
    </g>
    <polygon points="291,108 606,108 652,234 606,360 291,360 212,234" fill="none" stroke="var(--blue)" stroke-width="1"/>
    <g role="img" aria-label="Photo: smiling couple signing a property contract">
      <polygon points="297,114 600,114 645,234 600,354 297,354 219,234" fill="url(#gCouple)"/>
    </g>
    <polygon points="418,358 600,358 590,385 430,385" fill="none" stroke="#fff" stroke-width="1"/>
    <polygon points="594,164 676,164 706,237 676,311 594,311 624,237" fill="var(--blue)"/>
    <path d="M676 135L719 135M676 135L650 180M706 190L719 225M700 300L719 300" stroke="var(--blue)" stroke-width="1" fill="none"/>
    <g role="img" aria-label="Photo: hands holding a small model house">
      <circle cx="239" cy="372" r="50" fill="url(#gHouse)"/>
    </g>
    <line x1="182" y1="458" x2="182" y2="512" stroke="#bbb" stroke-width=".6"/>
  </svg>
  <div class="fold"></div>

  <h2 class="heading abs" style="left:20px;top:24px;font-size:18px">Who <b>are we?</b></h2>
  <div class="body-copy abs" style="left:20px;top:46px;width:336px">At Harbor Deed, we have the experience and skill to effectively handle simple and complex residential real estate closings throughout Florida. We regularly work with realtors, buyers, sellers, lenders and mortgage brokers in real estate transactions ranging from single family homes to condominiums and townhomes. The closing is the most important part of the process, and the culmination of everyone's hard work. As such, we dedicate ourselves to meticulous title and escrow work, as well as regular and detailed customer updates. We understand the parties each have conflicting schedules, as well as different demands on their time, and will provide the flexibility needed to accommodate everyone. Our pricing structure is also easy to understand. Please contact us for a simple quote, or a more detailed, estimated seller net sheet.</div>

  <div class="brand abs" style="left:28px;top:433px;font-size:11.5px"><span class="mark" style="width:9px;height:9px"></span>HARBOR DEED</div>
  <div class="abs" style="left:34px;top:461px">
    <div class="contact-title">Contact us</div>
    <div class="address" style="margin-top:3px;display:flex;gap:5px">
      <svg width="9" height="9" viewBox="0 0 10 10" style="fill:var(--blue);margin-top:1px"><path d="M5 0L10 5H8.5V10H6V7H4V10H1.5V5H0Z"/></svg>
      <span>120 Lantern Cove Avenue, Suite 4,<br>Bayview, Florida 30000</span>
    </div>
  </div>
  <ul class="contact-list abs" style="left:192px;top:450px">
    <li><svg viewBox="0 0 10 10"><path d="M2 0L4 2.5L3 4Q4.5 6.5 6 7L7.5 6L10 8L8.5 10Q2 9 0 1.5Z"/></svg>555 010-2846</li>
    <li><svg viewBox="0 0 10 10"><path d="M2 0H8V3H10V8H8V10H2V8H0V3H2ZM3 1V3H7V1ZM3 6V9H7V6Z"/></svg>555 010-3391</li>
    <li><svg viewBox="0 0 10 10"><path d="M0 2H10V8H0ZM1 3L5 6L9 3V2.8L5 5.4L1 2.8Z"/></svg>info@harbordeedfl.com</li>
    <li><svg viewBox="0 0 10 10"><circle cx="5" cy="5" r="4.5"/></svg>www.harbordeedfl.com</li>
  </ul>

  <div class="brand abs" style="left:466px;top:96px;font-size:13.5px"><span class="mark" style="width:12px;height:12px"></span>HARBOR DEED</div>

  <div class="tagline abs" style="left:360px;top:401px">
    <div class="intro">We take the Aggravation and Anxiety out of</div>
    <div class="big">BUYING, SELLING AND<br>REFINANCING PROPERTY</div>
    <div class="pill">A Florida Limited Liability Company</div>
    <div class="url">www.harbordeedfl.com</div>
  </div>
</section>

<!-- Inside spread -->
<section class="spread spread--inside">
  <svg class="art" width="719" height="512" viewBox="0 0 719 512">
    <defs>
      <linearGradient id="gSuit" x1="0" y1="0" x2="1" y2="1"><stop offset="0" stop-color="#3e5269"/><stop offset="1" stop-color="#0f1a2a"/></linearGradient>
      <linearGradient id="gKeys" x1="0" y1="0" x2="1" y2="1"><stop offset="0" stop-color="#f3ece6"/><stop offset="1" stop-color="#d6c2b2"/></linearGradient>
      <linearGradient id="gRoom" x1="0" y1="0" x2="1" y2="0"><stop offset="0" stop-color="#e8e5e2"/><stop offset="1" stop-color="#d9d2cc"/></linearGradient>
      <linearGradient id="gHome" x1="0" y1="0" x2="0" y2="1"><stop offset="0" stop-color="#b8cfe0"/><stop offset=".6" stop-color="#b7a87f"/><stop offset="1" stop-color="#5f7d45"/></linearGradient>
      <linearGradient id="gHall" x1="0" y1="0" x2="1" y2="1"><stop offset="0" stop-color="#8a7258"/><stop offset="1" stop-color="#3d3026"/></linearGradient>
    </defs>
    <g role="img" aria-label="Photo: businessman cupping hands over a small house icon">
      <polygon points="0,0 232,0 262,78 225,156 0,156" fill="url(#gSuit)"/>
    </g>
    <g role="img" aria-label="Photo: hand passing a set of house keys to another hand">
      <polygon points="238,0 353,0 390,78 353,155 270,155 232,78" fill="url(#gKeys)"/>
    </g>
    <polygon points="355,0 372,0 410,78 372,156 355,156 392,78" fill="var(--blue)"/>
    <polygon points="230,125 258,125 246,150 218,150" fill="var(--blue)"/>
    <g role="img" aria-label="Photo: agent shaking hands with a couple in a bright living room">
      <polygon points="400,0 719,0 719,149 430,149 375,70" fill="url(#gRoom)"/>
    </g>
    <path d="M395 0L358 70L400 150" stroke="var(--blue)" stroke-width="1" fill="none"/>
    <rect x="0" y="476" width="719" height="36" fill="var(--slate)"/>
    <g role="img" aria-label="Photo: two-storey suburban home with a lawn">
      <polygon points="253,381 395,381 412,440 395,497 253,497 226,440" fill="url(#gHome)"/>
    </g>
    <g role="img" aria-label="Photo: family house with a front garden">
      <polygon points="446,437 568,437 590,475 568,512 446,512 418,475" fill="url(#gHome)"/>
    </g>
    <polygon points="412,318 548,318 566,372 548,427 412,427 394,372" fill="var(--blue)"/>
    <polygon points="404,312 556,312 576,372 556,433 404,433 386,372" fill="none" stroke="var(--blue)" stroke-width=".8"/>
    <g role="img" aria-label="Photo: elegant home interior with a grand staircase">
      <polygon points="596,380 708,380 719,400 719,482 596,482 575,430" fill="url(#gHall)"/>
    </g>
  </svg>
  <div class="fold"></div>

  <h2 class="apart-title abs" style="left:26px;top:136px">We sets <b>us apart</b></h2>
  <div class="apart-box abs" style="left:18px;top:165px;width:157px;height:300px">
    <p>At Harbor Deed LLC, we understand the importance of having the support of your Title Company whenever you need it. Because of this, we have developed cutting edge tools to help you provide the best service possible to your Buyers and Sellers.</p>
    <p>With over 11 years of experience in Title and Real Estate Law, we have the knowledge and follow through to ensure that your closing is successful and as headache free as possible.</p>
    <h4>Some of our innovations include:</h4>
    <ul class="innovations">
      <li><svg viewBox="0 0 10 10"><path d="M5 0L10 5H8.5V10H1.5V5H0Z"/></svg><span>Comprehensive Realtor/Lender Portal with immediate secure access to documents and status updates</span></li>
      <li><svg viewBox="0 0 10 10"><path d="M5 0L10 5H8.5V10H1.5V5H0Z"/></svg><span>24/7 Net Sheet and Buyer Cost Estimator App with the ability to Order Title with the click of a button</span></li>
      <li><svg viewBox="0 0 10 10"><path d="M5 0L10 5H8.5V10H1.5V5H0Z"/></svg><span>Digital Closing Package for Buyers and Sellers with secure online access to all closing documents post closing</span></li>
      <li><svg viewBox="0 0 10 10"><path d="M5 0L10 5H8.5V10H1.5V5H0Z"/></svg><span>Complimentary Post Closing Marketing Support for REALTORS and Lenders!</span></li>
    </ul>
    <p class="note">Evening and Mobile Closings Available!</p>
  </div>

  <h2 class="heading abs" style="left:190px;top:154px;font-size:19px">Realtor <b>Services</b></h2>
  <div class="abs" style="left:191px;top:184px;width:157px">
    <p class="lead">We provide knowledge and support during the entire closing process to ensure a successful transaction for you and your clients.</p>
    <div class="body-copy" style="margin-top:8px">
      <p>Harbor Deed recognizes the importance of your reputation. Whether you are a seasoned agent with a high quality reputation to protect, or a new agent intent on building a respected name for yourself, Harbor Deed knows your livelihood depends on the quality of your name. Our title and escrow work is meticulous, and our discretion is second to none.</p>
      <p>We pride ourselves on timely, accurate communication and the trust that results from it. Our ability to tailor the transaction to you and your client is the bedrock of our company.</p>
      <p>Ask yourself what your current title company has done to contribute to your success lately? The importance of working with a strategically competitive agency in today's market has never been more essential to anyone's success. Harbor Deed has the experience, attention to detail and dedication to grow your bottom line.</p>
    </div>
  </div>

  <h2 class="heading abs" style="left:381px;top:170px;font-size:19px">Lender <b>Services</b></h2>
  <div class="abs" style="left:382px;top:200px;width:317px">
    <p class="lead" style="font-weight:400;font-size:7.6px"><b>Harbor Deed works with national lenders, as well as local community banks and mortgage brokers.</b></p>
    <div class="body-copy" style="margin-top:9px;font-size:6.8px">We have an extensive vendor network to ensure your client's transactions close on time with only the highest level of customer service. We handle all types of loans including Purchases, Refinances, 1st and 2nd Mortgages, HELOCs, Construction loans, FHA loans and VA loans. Our title services include: title search, title examination, title commitment, title clearance, payoff/lien orders, escrow and closing services, recording, post-closing payoff tracking and title policy issuance. We are in full compliance with the Consumer Financial Protection Bureau regulations, as well as industry Best Practices, and our DeskClose closing software is designed to promptly provide you with the most up to date fee and title information.</div>
  </div>

  <div class="seal abs" style="left:394px;top:330px;width:172px">
    <span>ATTORNEY</span><b>OWNED AND</b><span>OPERATED</span>
  </div>

  <div class="footer-band" style="width:360px;background:transparent">www.harbordeedfl.com</div>
</section>

</body>
</html>
```